Dental Hygiene referral cards

I am looking to make some referral cards for our hygienists for our dental office. something with our logo and address on the front, and on the back have
hygienist:
__________________
Referred by:
__________________
with a little blurb about what we will give away for a referral.

attached to this is our logo, and a drawing of what im looking for.

I will need this for two of our offices, so just the logo and address will change.

```html
<!DOCTYPE html>
<html lang="en">
<head>
<meta charset="utf-8">
<title>Harbourline Dental – Referral Card</title>
<link rel="stylesheet" href="https://fonts.googleapis.com/css2?family=Lato:wght@400;700&family=Montserrat:wght@400;700&display=swap">
<style>
  :root {
    --navy: #16457f;
    --white: #ffffff;
    --grey: #9a9a9a;
    --ink: #333333;
    --backdrop: #e9eaec;
  }
  * { box-sizing: border-box; margin: 0; padding: 0; }
  html, body { width: 1200px; height: 780px; overflow: hidden; }
  body {
    background: var(--backdrop);
    display: flex;
    align-items: center;
    justify-content: center;
    gap: 40px;
    font-family: "Lato", sans-serif;
  }
  .card {
    position: relative;
    width: 540px;
    height: 310px;
    box-shadow: 0 6px 18px rgba(0,0,0,0.18);
  }
  .card__lines { position: absolute; inset: 0; }

  /* Referral side */
  .card--referral { background: var(--navy); color: var(--white); text-transform: uppercase; }
  .offer-title {
    position: absolute; left: 30px; top: 40px;
    font-size: 19px; font-weight: 700; line-height: 1.15; letter-spacing: 0.5px;
  }
  .field-label {
    position: absolute; right: 28px;
    font-size: 13px; letter-spacing: 0.8px;
  }
  .field-label--hygienist { top: 38px; font-size: 17px; font-weight: 700; }
  .field-label--referrer { top: 112px; }
  .offer-blurb {
    position: absolute; right: 24px; top: 208px; width: 300px;
    font-size: 10.5px; line-height: 1.7; letter-spacing: 0.4px; text-align: center;
  }

  /* Contact side */
  .card--contact { background: var(--white); }
  .brand {
    position: absolute; left: 14px; top: 14px; width: 196px; height: 282px;
    display: flex; flex-direction: column; align-items: center; justify-content: center; gap: 14px;
  }
  .brand__mark { width: 30px; height: 30px; border-radius: 50%; background: var(--navy); }
  .brand__name {
    font-family: "Lato", sans-serif; font-weight: 700; color: var(--navy);
    font-size: 22px; letter-spacing: 2px; text-transform: uppercase; text-align: center; line-height: 1.25;
  }
  .contact {
    position: absolute; left: 216px; top: 14px; width: 310px; height: 282px;
    display: flex; flex-direction: column; align-items: center; justify-content: center;
    text-align: center; font-family: "Lato", sans-serif; color: var(--ink);
  }
  .contact__name { font-family: "Montserrat", sans-serif; font-weight: 700; color: var(--navy); font-size: 23px; }
  .contact__role { font-family: "Montserrat", sans-serif; color: var(--grey); font-size: 15px; margin-top: 2px; }
  .contact__icons { display: flex; gap: 5px; margin: 12px 0 8px; }
  .contact__icons svg { width: 16px; height: 16px; }
  .contact__details { font-size: 11.5px; line-height: 1.45; }
  .contact__rule { width: 56px; height: 2px; background: var(--navy); margin: 10px 0; }
  .contact__address { font-size: 11.5px; line-height: 1.45; }
</style>
</head>
<body>

  <section class="card card--referral" aria-label="Referral side">
    <svg class="card__lines" viewBox="0 0 540 310" aria-hidden="true">
      <g fill="none" stroke="var(--white)" stroke-width="1.6">
        <rect x="12" y="12" width="516" height="286"/>
        <line x1="232" y1="12" x2="140" y2="298"/>
        <line x1="205" y1="96" x2="528" y2="96"/>
        <line x1="172" y1="196" x2="528" y2="196"/>
      </g>
    </svg>
    <h2 class="offer-title">Free<br>Brightwave<br>Toothbrush !</h2>
    <p class="field-label field-label--hygienist">Hygienist</p>
    <p class="field-label field-label--referrer">Referred by :</p>
    <p class="offer-blurb">Refer a patient an exam and a cleaning and both of you will receive a free Brightwave toothbrush !</p>
  </section>

  <section class="card card--contact" aria-label="Contact side">
    <svg class="card__lines" viewBox="0 0 540 310" aria-hidden="true">
      <g fill="none" stroke="var(--navy)" stroke-width="1.6">
        <rect x="14" y="14" width="512" height="282"/>
        <line x1="214" y1="14" x2="214" y2="296"/>
      </g>
    </svg>

    <div class="brand">
      <span class="brand__mark" aria-hidden="true"></span>
      <p class="brand__name">Harbourline<br>Dental</p>
    </div>

    <div class="contact">
      <p class="contact__name">Dana Whitford</p>
      <p class="contact__role">President</p>
      <div class="contact__icons" aria-hidden="true">
        <svg viewBox="0 0 16 16"><circle cx="8" cy="8" r="8" fill="var(--navy)"/><path d="M5 4.5l1.6-.4.8 2-1 .8a5 5 0 0 0 2.7 2.7l.8-1 2 .8-.4 1.6c-3.5.3-6.8-3-6.5-6.5z" fill="var(--white)"/></svg>
        <svg viewBox="0 0 16 16"><circle cx="8" cy="8" r="8" fill="var(--navy)"/><rect x="5.5" y="3.5" width="5" height="9" rx="1" fill="none" stroke="var(--white)" stroke-width="1.2"/></svg>
        <svg viewBox="0 0 16 16"><circle cx="8" cy="8" r="8" fill="var(--navy)"/><rect x="4" y="5" width="8" height="6" fill="none" stroke="var(--white)" stroke-width="1.1"/><path d="M4 5l4 3.2L12 5" fill="none" stroke="var(--white)" stroke-width="1.1"/></svg>
        <svg viewBox="0 0 16 16"><circle cx="8" cy="8" r="8" fill="var(--navy)"/><circle cx="8" cy="8" r="4" fill="none" stroke="var(--white)" stroke-width="1.1"/><path d="M4 8h8M8 4c-2 2.5-2 5.5 0 8M8 4c2 2.5 2 5.5 0 8" fill="none" stroke="var(--white)" stroke-width="0.9"/></svg>
      </div>
      <p class="contact__details">
        (555) 014-2281<br>
        (555) 014-7390<br>
        hello@harbourlinedental.com<br>
        www.harbourlinedental.com
      </p>
      <span class="contact__rule" aria-hidden="true"></span>
      <p class="contact__address">Unit 4, 18 Tallow Street,<br>Kestrel Bay SA 5999</p>
    </div>
  </section>

</body>
</html>
```